依頼詳細
展示会の会場を歩いているお客様に一目でこの商品がどのようなものかを理解していただけるような、わかりやすく、目を引くインパクトのあるデザインを希望します。
記載項目
商品名(点検口の安全金網 Rフレア)/社名/キャッチコピー/ロゴ
詳細は添付ファイル参照
サイズ
B1(縦横どちらも可)
ページ数
片面
希望イメージ
シンプル 複雑
単色 カラフル
暗い 明るい
日常 高級
遊び心 厳粛
未来的 伝統的
女性的 男性的
希望する色
オレンジ(黄色めの)と黒 その他の色も可
納品ファイル
• 高解像度JPG (.jpg)
• イラストレーター形式 (.ai)
補足説明
Rフレア http://item.sorabazaar.jp/lumo-shop/c/0000000830/
点検口 http://item.sorabazaar.jp/lumo-shop/c/0000000480/

```html
<!DOCTYPE html>
<html lang="ja">
<head>
<meta charset="utf-8">
<title>点検口の安全金網 Rフレア</title>
<link rel="stylesheet" href="https://fonts.googleapis.com/css2?family=Noto+Sans+JP:wght@500;700;900&display=swap">
<style>
  :root {
    --navy: #0a1733;
    --navy-deep: #050c1f;
    --accent-red: #d8261f;
    --white: #ffffff;
    --sky: #1f6fd6;
    --yellow: #ffe600;
    --ink: #111111;
    --photo-orange: #c9664a;
    --photo-green: #6fae3c;
  }
  html, body {
    margin: 0;
    padding: 0;
    width: 849px;
    height: 1200px;
    overflow: hidden;
    background: var(--white);
    font-family: "Noto Sans JP", sans-serif;
  }
  .poster {
    position: relative;
    width: 849px;
    height: 1200px;
    overflow: hidden;
    background: var(--navy-deep);
  }
  .hero-photo {
    position: absolute;
    inset: 0 0 210px 0;
    background:
      radial-gradient(circle at 78% 22%, rgba(80,200,160,.55) 0, transparent 22%),
      radial-gradient(circle at 60% 48%, var(--photo-green) 0, transparent 18%),
      radial-gradient(ellipse at 62% 40%, var(--photo-orange) 0, rgba(201,102,74,.7) 30%, transparent 46%),
      radial-gradient(circle at 88% 60%, rgba(60,120,220,.6) 0, transparent 20%),
      linear-gradient(135deg, var(--navy-deep) 0%, var(--navy) 45%, #13325a 100%);
  }
  .mesh-photo {
    position: absolute;
    left: 55px;
    top: 760px;
    width: 460px;
    height: 230px;
    border-radius: 8px;
    background: linear-gradient(160deg, #d9dde2 0%, #9aa3ad 55%, #5b6570 100%);
    opacity: .9;
  }
  .headline {
    position: absolute;
    left: 160px;
    top: 70px;
    margin: 0;
    color: var(--white);
    font-weight: 900;
    line-height: 1.1;
  }
  .headline .lead { display: block; font-size: 54px; letter-spacing: 2px; }
  .headline .key {
    display: block;
    font-size: 104px;
    letter-spacing: 2px;
    -webkit-text-stroke: 3px var(--white);
    paint-order: stroke fill;
  }
  .headline .key em { font-style: normal; color: var(--accent-red); }
  .headline .tail { display: block; font-size: 70px; }
  .product-tag {
    position: absolute;
    left: 610px;
    top: 662px;
    width: 195px;
    padding: 6px 8px;
    background: var(--navy);
    border: 2px solid var(--white);
    color: var(--white);
    font-weight: 700;
    font-size: 15px;
    line-height: 1.3;
  }
  .product-tag strong { display: block; font-size: 26px; font-weight: 900; }
  .mission {
    position: absolute;
    left: 180px;
    top: 735px;
    margin: 0;
    color: var(--white);
    font-size: 23px;
    font-weight: 700;
  }
  .mission em { font-style: normal; color: #ff4a3d; }
  .features {
    position: absolute;
    left: 520px;
    top: 790px;
    margin: 0;
    padding: 0;
    list-style: none;
    color: var(--white);
    font-size: 20px;
    font-weight: 700;
    line-height: 1.6;
  }
  .price-badge {
    position: absolute;
    left: 482px;
    top: 928px;
    display: flex;
    align-items: center;
    gap: 10px;
  }
  .price-badge .also {
    background: var(--yellow);
    color: var(--ink);
    font-weight: 900;
    font-size: 20px;
    padding: 2px 10px;
    border-radius: 14px;
  }
  .price-badge .low {
    background: var(--white);
    color: var(--navy);
    font-weight: 900;
    font-size: 34px;
    padding: 0 16px;
  }
  .name-band {
    position: absolute;
    left: 0;
    top: 990px;
    width: 849px;
    height: 58px;
    background: var(--navy);
    color: var(--white);
    font-weight: 900;
    font-size: 36px;
    line-height: 58px;
    text-align: center;
    letter-spacing: 2px;
  }
  .name-band strong { font-size: 46px; margin-left: 10px; }
  .slogan-band {
    position: absolute;
    left: 0;
    top: 1048px;
    width: 849px;
    height: 80px;
    background: var(--sky);
    color: var(--white);
    font-weight: 900;
    font-size: 58px;
    line-height: 80px;
    text-align: center;
    letter-spacing: 3px;
  }
  .company {
    position: absolute;
    left: 0;
    top: 1128px;
    width: 849px;
    height: 72px;
    background: var(--white);
    color: var(--ink);
    font-weight: 900;
    font-size: 34px;
    line-height: 72px;
    text-align: center;
  }
</style>
</head>
<body>
  <main class="poster">
    <div class="hero-photo" role="img" aria-label="オレンジ色の点検口ボックスに安全金網を取り付けた製品写真、背景はカラフルなボケ"></div>
    <div class="mesh-photo" role="img" aria-label="取り外した安全金網単体の製品写真"></div>

    <h1 class="headline">
      <span class="lead">点検口の向こうには</span>
      <span class="key"><em>重要</em>と<em>危険</em>が</span>
      <span class="tail">待機中ー</span>
    </h1>

    <div class="product-tag">点検口の安全金網<strong>Rフレア</strong></div>

    <p class="mission">現場の作業者を<em>機械の巻込まれ事故</em>から守る!</p>

    <ul class="features">
      <li>工具の落下や手足の侵入を防止</li>
      <li>面倒な溶接不要で簡単!</li>
      <li>3分で取付け取外し!</li>
    </ul>

    <div class="price-badge">
      <span class="also">しかも</span>
      <span class="low">ローコスト!</span>
    </div>

    <div class="name-band">点検口の安全金網<strong>Rフレア</strong></div>
    <div class="slogan-band">現場の守りは万全か?!</div>
    <div class="company">株式会社ルモテック</div>
  </main>
</body>
</html>
```